Brevin Electric Ltd

Looking for a single page website and Facebook page design. I am an electrical contractor based on Vancouver Island. I do service, custom homes, residential and commercial installations. My company just started out, so I don't have any pictures of installs yet. I have 25 years experience. I would like the colors to be my logo colors black and I have a black Torvik Ridgeman that will be my vehicle which I will have a wrap for.
Updates

I just posted the contest today, not sure why the deadline is the same day.

Went on vacation/holiday

Industry/Entity Type

Electrician

Requirements
Must have
• Services provided, About me section, quote section,
Nice to have
• I am not quite sure yet, I need to see some designs first .

```html
<!DOCTYPE html>
<html lang="en">
<head>
<meta charset="UTF-8">
<title>Brevin Electric Ltd — Cover</title>
<link rel="stylesheet" href="https://fonts.googleapis.com/css2?family=Montserrat:wght@500;600;700&family=Open+Sans:wght@400&display=swap">
<style>
  :root {
    --ink: #141414;
    --yellow: #f4b400;
    --white: #ffffff;
    --text-soft: #d9d9d9;
    --photo-dark: #2b2b2b;
    --photo-mid: #6d6f72;
    --photo-light: #b9bcc0;
  }
  * { margin: 0; padding: 0; box-sizing: border-box; }
  html, body { width: 1200px; height: 444px; overflow: hidden; background: var(--ink); }
  .cover {
    position: relative;
    width: 1200px;
    height: 444px;
    background: var(--ink);
    overflow: hidden;
    font-family: "Open Sans", sans-serif;
    color: var(--white);
  }
  .cover__shapes { position: absolute; inset: 0; width: 1200px; height: 444px; }
  .brand-mark {
    position: absolute;
    left: 186px;
    top: 88px;
    display: flex;
    align-items: center;
    gap: 12px;
    font-family: "Montserrat", sans-serif;
    font-weight: 700;
    font-size: 34px;
    letter-spacing: 1px;
    color: var(--yellow);
  }
  .brand-mark__dot {
    width: 22px; height: 22px;
    border-radius: 50%;
    background: var(--yellow);
  }
  .company-name {
    position: absolute;
    left: 120px;
    top: 196px;
    font-family: "Montserrat", sans-serif;
    font-weight: 600;
    font-size: 26px;
    letter-spacing: 0.5px;
    color: var(--white);
  }
  .company-name__accent { color: var(--yellow); }
  .divider {
    position: absolute;
    left: 120px;
    top: 268px;
    width: 90px;
    height: 3px;
    background: var(--yellow);
  }
  .services {
    position: absolute;
    left: 120px;
    top: 283px;
    width: 480px;
    font-size: 16px;
    line-height: 22px;
    color: var(--text-soft);
  }
  .join-button {
    position: absolute;
    left: 120px;
    top: 361px;
    width: 78px;
    height: 22px;
    border-radius: 3px;
    background: var(--yellow);
    color: var(--ink);
    font-family: "Montserrat", sans-serif;
    font-weight: 700;
    font-size: 12px;
    line-height: 22px;
    text-align: center;
    letter-spacing: 0.5px;
  }
  .contact-row {
    position: absolute;
    left: 120px;
    top: 391px;
    width: 520px;
    height: 20px;
    font-size: 13px;
    letter-spacing: 1.2px;
    color: var(--text-soft);
  }
  .contact-row__web { position: absolute; left: 0; top: 1px; }
  .social {
    position: absolute;
    left: 262px;
    top: 1px;
    display: flex;
    gap: 6px;
  }
  .social__dot {
    width: 17px; height: 17px;
    border-radius: 50%;
    background: var(--yellow);
  }
  .contact-row__handle { position: absolute; left: 360px; top: 1px; }
</style>
</head>
<body>
  <div class="cover">
    <svg class="cover__shapes" viewBox="0 0 1000 370" preserveAspectRatio="none" aria-hidden="false">
      <defs>
        <linearGradient id="photoTone" x1="0" y1="0" x2="1" y2="1">
          <stop offset="0" stop-color="var(--photo-mid)"/>
          <stop offset="0.45" stop-color="var(--photo-light)"/>
          <stop offset="1" stop-color="var(--photo-dark)"/>
        </linearGradient>
      </defs>
      <polygon class="band-left" points="0,160 72,370 0,370" fill="var(--yellow)"/>
      <polygon class="band-top" points="482,0 557,0 630,238 602,238" fill="var(--yellow)"/>
      <polygon class="photo" role="img" aria-label="Photo of an electrician in gloves testing a wired electrical panel with a multimeter probe"
               points="557,0 1000,0 1000,370 660,370 600,190" fill="url(#photoTone)"/>
      <polygon class="band-glass" points="592,140 645,140 725,370 668,370" fill="var(--yellow)" fill-opacity="0.55"/>
      <polygon class="band-corner" points="835,0 880,0 902,55 860,55" fill="var(--yellow)"/>
      <polygon class="band-right" points="893,128 1000,128 1000,370 975,370" fill="var(--yellow)"/>
      <polygon class="band-foot" points="607,295 640,295 665,370 632,370" fill="var(--yellow)"/>
    </svg>

    <div class="brand-mark"><span class="brand-mark__dot"></span>BREVIN</div>

    <h1 class="company-name">BREVIN <span class="company-name__accent">ELECTRIC</span> Ltd</h1>
    <div class="divider"></div>
    <p class="services">We do service, custom homes, residential and commercial installations</p>

    <div class="join-button">JOIN US</div>

    <div class="contact-row">
      <span class="contact-row__web">www.websitename.com</span>
      <div class="social">
        <span class="social__dot"></span>
        <span class="social__dot"></span>
        <span class="social__dot"></span>
        <span class="social__dot"></span>
      </div>
      <span class="contact-row__handle">/ brandname</span>
    </div>
  </div>
</body>
</html>
```